Business Card design for a skin clinic

i would like a business card design for our skin clinic.
our logo colors are Blue and Grey and Bule /white.
we are searching for a minimalistic design yet very elegant,dynamic and professional which can reflect a professional medical skin care clinic( not a beauty salon).
THE DESGIN IS NOT FOR A PERSON IT WILL BE USED IN THE CLINIC FOR CLIENTS SO THERE SHOULD BE NO NAME OF A PERSON ONLY THE CLINIC NAME AND THE CONTACT INFO

Target Market(s)
young and old womens
Industry/Entity Type
Business
Contact Information for Business Card
we have 2 address and both should be on the card.
address A: Lindenhofkade 42B, 3017KP Rotterdam, Tel 010 438 21 95
address B: Zonnewijzerstraat 73, 1062HT Amsterdam Tel 020 519 8372
website www.velorahuid.nu, email info@velorahuid.nu
Look and feel

```html
<!DOCTYPE html>
<html lang="nl">
<head>
<meta charset="utf-8">
<title>Velorahuid – business card</title>
<link href="https://fonts.googleapis.com/css2?family=Montserrat:wght@300;400;500&display=swap" rel="stylesheet">
<style>
  :root {
    --bg: #d9dcdf;
    --card: #f4f5f5;
    --blue: #3b78c0;
    --grey: #5d6166;
    --grey-light: #8a8e93;
  }
  * { box-sizing: border-box; margin: 0; padding: 0; }
  html, body { width: 1200px; height: 900px; overflow: hidden; }
  body {
    background: var(--bg);
    font-family: "Montserrat", sans-serif;
    display: flex;
    flex-direction: column;
    align-items: center;
    justify-content: center;
    gap: 40px;
  }
  .card {
    position: relative;
    width: 600px;
    height: 370px;
    background: var(--card);
    box-shadow: 0 2px 10px rgba(0,0,0,0.12);
  }
  /* front */
  .front-brand {
    position: absolute;
    left: 120px;
    top: 120px;
  }
  .wordmark {
    color: var(--blue);
    font-weight: 400;
    letter-spacing: 0.06em;
    text-transform: uppercase;
  }
  .front-brand .wordmark { font-size: 46px; }
  .tagline {
    margin-top: 10px;
    margin-left: 60px;
    color: var(--grey);
    font-size: 17px;
    font-weight: 400;
    letter-spacing: 0.04em;
  }
  .website {
    margin-top: 22px;
    margin-left: 100px;
    color: var(--grey-light);
    font-size: 13px;
    font-weight: 400;
    letter-spacing: 0.32em;
    text-transform: uppercase;
  }
  /* back */
  .back-brand {
    position: absolute;
    right: 60px;
    top: 56px;
  }
  .back-brand .wordmark { font-size: 28px; }
  .edge-square {
    position: absolute;
    right: 0;
    top: 150px;
    width: 22px;
    height: 22px;
    background: var(--blue);
  }
  .email {
    position: absolute;
    right: 60px;
    top: 200px;
    color: var(--grey);
    font-size: 16px;
    font-weight: 300;
    letter-spacing: 0.03em;
  }
  .addresses {
    position: absolute;
    left: 56px;
    bottom: 40px;
    color: var(--grey);
    font-size: 14px;
    font-weight: 300;
    line-height: 1.5;
    font-style: normal;
  }
  .location + .location { margin-top: 20px; }
  .location .tel { margin-top: 10px; }
</style>
</head>
<body>
  <section class="card card-front" aria-label="Card front">
    <div class="front-brand">
      <div class="wordmark">Velorahuid</div>
      <div class="tagline">next generation skin care</div>
      <div class="website">www.velorahuid.nu</div>
    </div>
  </section>

  <section class="card card-back" aria-label="Card back">
    <div class="back-brand"><div class="wordmark">Velorahuid</div></div>
    <div class="edge-square"></div>
    <div class="email">info@velorahuid.nu</div>
    <address class="addresses">
      <div class="location">
        <div>Zonnewijzerstraat 73</div>
        <div>1062HT Amsterdam</div>
        <div class="tel">Tel : 020 519 8372</div>
      </div>
      <div class="location">
        <div>Lindenhofkade 42B</div>
        <div>3017KP Rotterdam</div>
        <div class="tel">Tel : 010 438 21 95</div>
      </div>
    </address>
  </section>
</body>
</html>
```